Velmorique needs a elegant mystical business card design

The theme of Velmorique is centered on Kemetic/Ancient Egyptian Spirituality. My business sells handmade scented candles, mystic oils, body sprays, tarot readings and more. I would like my business card to reflect an elegant and mystical look. Hieroglyphs around the borders would be a cool idea. Also, the main colors I am working with is Black and Gold= colors of royalty. Black background. The business card will be double sided. The back will have the logo, and the front will have the basic information (ie name, title, business, phone, email, website, etc..)

Target Market(s)

The target market are people into metaphysics, holistic healing, ancient Egyptian culture, aromatherapy, occult science, and the esoteric.

Industry/Entity Type

Business

Contact Information for Business Card

Name: Marlonda T. Pruitt
Title: Owner
Business: VELMORIQUE
Phone: 917.302.4417
Website: www.Velmorique.net
Facebook, Instagram, and twitter icons

Font styles to use
Serif
Decorative

Requirements
Must have
• My logo, and website.
Nice to have
• Ancient Egyptian hieroglyphs, Elegant designs around the border, or encircling the logo.

```html
<!DOCTYPE html>
<html lang="en">
<head>
<meta charset="utf-8">
<title>Velmorique Business Card</title>
<link rel="stylesheet" href="https://fonts.googleapis.com/css2?family=Cinzel:wght@400;600&family=Open+Sans:wght@400&display=swap">
<style>
  :root {
    --stage: #2b2c31;
    --card-black: #050505;
    --gold-deep: #8a6a3a;
    --gold-mid: #b9975e;
    --gold-light: #e0c48e;
    --gold-text: #c9a66b;
    --gold-band: linear-gradient(180deg, var(--gold-deep) 0%, var(--gold-light) 45%, var(--gold-mid) 70%, var(--gold-deep) 100%);
  }
  * { box-sizing: border-box; margin: 0; padding: 0; }
  html, body { width: 1200px; height: 900px; overflow: hidden; }
  body { background: var(--stage); position: relative; font-family: "Open Sans", sans-serif; }

  .card {
    position: absolute;
    width: 620px;
    height: 354px;
    background: var(--card-black);
    overflow: hidden;
    box-shadow: 0 14px 30px rgba(0,0,0,0.55);
  }
  .card--back { left: 60px; top: 66px; }
  .card--front { left: 520px; top: 480px; }

  .glyph-band {
    position: absolute;
    left: 0; right: 0;
    background: var(--gold-band);
  }
  .rule {
    position: absolute;
    height: 2px;
    background: var(--gold-mid);
  }

  /* back side */
  .card--back .glyph-band--top { top: 0; height: 52px; }
  .card--back .rule--top { top: 62px; left: 0; right: 0; }
  .card--back .rule--mid { top: 232px; left: 0; right: 0; }
  .card--back .glyph-band--mid { top: 242px; height: 56px; }
  .card--back .rule--low { top: 308px; left: 0; right: 0; }
  .card--back .glyph-band--bottom { top: 318px; height: 36px; }

  .wordmark {
    position: absolute;
    left: 0; right: 0;
    text-align: center;
    font-family: "Cinzel", serif;
    font-weight: 600;
    color: var(--gold-text);
    letter-spacing: 0.12em;
  }
  .wordmark-dot {
    display: inline-block;
    width: 10px; height: 10px;
    border-radius: 50%;
    background: var(--gold-text);
    margin-right: 12px;
    vertical-align: middle;
  }
  .card--back .wordmark { top: 118px; font-size: 38px; }
  .website {
    position: absolute;
    left: 0; right: 0;
    top: 200px;
    text-align: center;
    font-family: "Cinzel", serif;
    font-size: 15px;
    color: var(--gold-text);
    letter-spacing: 0.04em;
  }

  /* front side */
  .card--front .rule--left { top: 232px; left: 0; width: 170px; transform: rotate(0deg); }
  .card--front .rule--right { top: 70px; right: 0; width: 120px; }
  .card--front .glyph-band--bottom { bottom: 0; height: 50px; }
  .card--front .wordmark { top: 48px; font-size: 32px; }
  .holder {
    position: absolute;
    left: 0; right: 0;
    top: 118px;
    text-align: center;
  }
  .holder-name {
    font-family: "Cinzel", serif;
    font-weight: 600;
    font-size: 20px;
    color: var(--gold-text);
    letter-spacing: 0.06em;
  }
  .holder-title {
    font-family: "Cinzel", serif;
    font-size: 12px;
    color: var(--gold-text);
    margin-top: 2px;
  }
  .contact {
    position: absolute;
    left: 190px;
    top: 186px;
    color: var(--gold-text);
    font-size: 14px;
    line-height: 22px;
  }
  .contact-line { display: flex; align-items: center; gap: 8px; }
  .contact-line svg { width: 14px; height: 14px; fill: var(--gold-text); }
  .social {
    position: absolute;
    left: 400px;
    top: 190px;
    display: flex;
    gap: 8px;
  }
  .social-tile {
    width: 22px; height: 22px;
    background: var(--gold-mid);
    border-radius: 2px;
  }
</style>
</head>
<body>

<section class="card card--back" aria-label="Card back">
  <div class="glyph-band glyph-band--top" role="img" aria-label="Gold band with embossed hieroglyph pattern"></div>
  <div class="rule rule--top"></div>
  <div class="wordmark"><span class="wordmark-dot"></span>VELMORIQUE</div>
  <div class="website">www.Velmorique.net</div>
  <div class="rule rule--mid"></div>
  <div class="glyph-band glyph-band--mid" role="img" aria-label="Gold band with embossed hieroglyph pattern"></div>
  <div class="rule rule--low"></div>
  <div class="glyph-band glyph-band--bottom" role="img" aria-label="Gold band with embossed hieroglyph pattern"></div>
</section>

<section class="card card--front" aria-label="Card front">
  <div class="rule rule--right"></div>
  <div class="wordmark"><span class="wordmark-dot"></span>VELMORIQUE</div>
  <div class="holder">
    <div class="holder-name">Marlonda T. Pruitt</div>
    <div class="holder-title">Owner</div>
  </div>
  <div class="rule rule--left"></div>
  <div class="contact">
    <div class="contact-line">
      <svg viewBox="0 0 16 16" aria-hidden="true"><path d="M3 1h3l1.5 4-2 1.2a9 9 0 0 0 4.3 4.3L11 8.5l4 1.5v3c0 1-1 2-2 2A13 13 0 0 1 1 3c0-1 1-2 2-2z"/></svg>
      <span>917.302.4417</span>
    </div>
    <div class="contact-line">
      <svg viewBox="0 0 16 16" aria-hidden="true"><path d="M1 3h14v10H1z M2 4l6 5 6-5" fill="none" stroke="#c9a66b" stroke-width="1.4"/></svg>
      <span>marlonda@velmorique.net</span>
    </div>
  </div>
  <div class="social" role="img" aria-label="Social media links">
    <span class="social-tile"></span>
    <span class="social-tile"></span>
    <span class="social-tile"></span>
  </div>
  <div class="glyph-band glyph-band--bottom" role="img" aria-label="Gold band with embossed hieroglyph pattern"></div>
</section>

</body>
</html>
```